Looking for a high-end business card design for a construction company

We are looking to update our business card design. We are a post-frame construction company that builds custom buildings, commercial spaces, homes, and anything else. We have multiple people working here so we would need something we can easily customize the information for the specific person. We need a name, website, cell phone, office phone as well as social icons. Our colors are black, white, and grey/silver so I would love a black background or something that is more striking than just a traditional white business card. Looking for something that is very professional with a high-end look/feel. I have attached our logos, they can be silver, white, grey, or black.
Industry/Entity Type
Construction
Contact Information for Business Card
Business logo, Name, Cell phone, Office phone, website, social Icons
Colors
Designer to choose only greyscale colors for use in the design.
Look and feel

```html
<!DOCTYPE html>
<html lang="en">
<head>
<meta charset="utf-8">
<title>Hartwell Builders business card</title>
<link href="https://fonts.googleapis.com/css2?family=Open+Sans:wght@400;600;700&display=swap" rel="stylesheet">
<style>
  :root{
    --backdrop:#3b3b3b;
    --card:#121212;
    --card-edge:#1c1c1c;
    --silver:#d9d9d9;
    --silver-dim:#a9a9a9;
    --rule:#8c8c8c;
    --pattern-dark:#0b0b0b;
    --pattern-light:#1e1e1e;
  }
  *{margin:0;padding:0;box-sizing:border-box}
  html,body{width:1200px;height:801px;overflow:hidden}
  body{
    background:var(--backdrop);
    font-family:"Open Sans",Arial,sans-serif;
    display:flex;align-items:center;justify-content:center;gap:40px;
  }
  .card{
    width:520px;height:297px;background:var(--card);
    border:1px solid var(--card-edge);position:relative;overflow:hidden;
  }
  /* front */
  .brand{
    position:absolute;top:62px;left:0;right:0;
    display:flex;align-items:center;justify-content:center;gap:14px;
    color:var(--silver);font-weight:700;
  }
  .brand-dot{width:34px;height:34px;border-radius:50%;background:var(--silver)}
  .brand-name{display:flex;flex-direction:column;line-height:1}
  .brand-name .main{font-size:30px;letter-spacing:5px}
  .brand-name .sub{font-size:13px;letter-spacing:3.2px;margin-top:5px}
  .details{
    position:absolute;top:158px;left:0;right:0;
    display:flex;justify-content:center;align-items:center;
  }
  .person{text-align:right;padding-right:22px;width:230px}
  .person-name{color:var(--silver);font-weight:600;font-size:17px;letter-spacing:.5px}
  .person-title{color:var(--silver-dim);font-size:12px;margin-top:2px}
  .divider{width:1px;height:86px;background:var(--rule)}
  .contact{list-style:none;padding-left:20px;width:250px}
  .contact li{display:flex;align-items:center;gap:8px;color:var(--silver);font-size:11.5px;line-height:20px}
  .contact svg{width:11px;height:11px;flex:none;fill:none;stroke:var(--silver);stroke-width:1.6}
  /* back */
  .pattern{position:absolute;inset:0;background:linear-gradient(135deg,var(--pattern-dark),var(--pattern-light) 50%,var(--pattern-dark))}
  .back-brand{
    position:absolute;right:34px;bottom:54px;
    color:var(--silver);font-weight:700;font-size:15px;letter-spacing:3px;
  }
</style>
</head>
<body>
  <section class="card card-front">
    <div class="brand">
      <span class="brand-dot"></span>
      <div class="brand-name"><span class="main">HARTWELL</span><span class="sub">BUILDERS, INC.</span></div>
    </div>
    <div class="details">
      <div class="person">
        <p class="person-name">DAREN KOLBECK</p>
        <p class="person-title">President</p>
      </div>
      <div class="divider"></div>
      <ul class="contact">
        <li><svg viewBox="0 0 12 12"><rect x="3" y="1" width="6" height="10" rx="1"/></svg>555-014-2278</li>
        <li><svg viewBox="0 0 12 12"><path d="M2 2c0 5 3 8 8 8l1-2-2-1-1 1C6 7 5 6 4 4l1-1-1-2z"/></svg>555-014-2278</li>
        <li><svg viewBox="0 0 12 12"><rect x="1" y="2.5" width="10" height="7"/><path d="M1 2.5l5 4 5-4"/></svg>dkolbeck@hartwellbuilders</li>
        <li><svg viewBox="0 0 12 12"><circle cx="6" cy="6" r="5"/><path d="M1 6h10M6 1c-2.5 3-2.5 7 0 10M6 1c2.5 3 2.5 7 0 10"/></svg>www.hartwellbuilders.com</li>
      </ul>
    </div>
  </section>
  <section class="card card-back">
    <div class="pattern" role="img" aria-label="Tone-on-tone repeating monogram pattern in glossy black"></div>
    <p class="back-brand">HARTWELL</p>
  </section>
</body>
</html>
```